Velmora Care! Create an exciting flyer for our hemodialysis clinic

Create an engaging Flyer that shows our offering and that will drive patients to our hemodialysis clinic. www.velmoracare.example

Target Market(s)

Mass public

Industry/Entity Type

Healthcare

Requirements
Must have
• 1 Our logo. 2. Should include that we accept all insurances 3. Our tag line “Transforming Lives, One Dialysis Session at a Time.”

```html
<!DOCTYPE html>
<html lang="en">
<head>
<meta charset="utf-8">
<title>Velmora Care – In-Center Hemodialysis Clinic Flyer</title>
<link rel="stylesheet" href="https://fonts.googleapis.com/css2?family=Montserrat:ital,wght@0,400;0,500;0,700;0,800;1,700&display=swap">
<style>
  :root {
    --stage: #2f5f70;
    --paper: #ffffff;
    --blue: #1a7cc4;
    --navy: #0d4fa0;
    --green: #54a546;
    --ink: #1b1b1b;
    --room-light: #e4ebee;
    --room-cool: #bfcfd9;
    --room-green: #9ccb8a;
  }
  * { box-sizing: border-box; margin: 0; padding: 0; }
  html, body {
    width: 1200px; height: 927px; overflow: hidden;
    background: var(--stage);
    font-family: "Montserrat", sans-serif;
  }
  .canvas { position: relative; width: 1200px; height: 927px; }
  .flyer {
    position: absolute; left: 255px; top: 17px;
    width: 1097px; height: 1420px;
    background: var(--paper);
    transform: scale(0.629); transform-origin: 0 0;
    overflow: hidden;
    color: var(--ink);
  }
  .flyer > * { position: absolute; }
  .shapes { left: 0; top: 0; width: 1097px; height: 1420px; }

  .site-url { left: 89px; top: 52px; font-size: 20px; color: var(--blue); }

  .brand { left: 880px; top: 47px; width: 190px; text-align: center; }
  .brand-square {
    width: 74px; height: 74px; margin: 0 auto 16px;
    background: var(--green); border-radius: 4px;
  }
  .brand-name {
    font-size: 30px; font-weight: 700; color: var(--blue);
    letter-spacing: 1px; line-height: 1.05;
  }

  .hero-claim {
    left: 740px; top: 322px; width: 290px; text-align: center;
    color: #fff; font-size: 32px; line-height: 48px; font-weight: 400;
  }
  .hero-claim strong { font-weight: 700; display: block; }

  .headline { left: 112px; top: 694px; color: var(--blue); }
  .headline .kicker { display: block; font-size: 53px; font-weight: 500; line-height: 62px; }
  .headline .title { display: block; font-size: 67px; font-weight: 800; line-height: 80px; }
  .headline .title span { font-weight: 500; }

  .body-copy { left: 114px; top: 882px; font-size: 21.5px; line-height: 26px; white-space: nowrap; }
  .body-copy p { margin-bottom: 25px; }

  .tagline {
    left: 150px; top: 1117px; font-size: 20px; font-weight: 700;
    font-style: italic; color: #fff;
  }

  .insurance-pill {
    left: 200px; top: 1226px; width: 236px; height: 80px;
    background: var(--navy); border-radius: 0 40px 40px 0;
    padding: 8px 0 0 46px; color: #fff; font-size: 24px; line-height: 30px;
  }
  .insurance-shield { left: 112px; top: 1198px; width: 118px; height: 136px; }

  .call-prompt { left: 596px; top: 1250px; font-size: 24px; }

  .phone {
    left: 586px; top: 1322px; display: flex; align-items: center; gap: 14px;
    color: #fff; font-size: 52px; font-weight: 700;
  }
  .phone svg { width: 40px; height: 40px; }
</style>
</head>
<body>
<div class="canvas">
  <div class="flyer">
    <svg class="shapes" viewBox="0 0 1097 1420">
      <defs>
        <linearGradient id="heroTone" x1="0" y1="0" x2="1" y2="0">
          <stop offset="0" stop-color="var(--room-cool)"/>
          <stop offset="0.45" stop-color="var(--room-light)"/>
          <stop offset="0.62" stop-color="var(--room-green)"/>
          <stop offset="0.75" stop-color="var(--green)"/>
        </linearGradient>
      </defs>
      <path role="img" aria-label="Photo: a smiling doctor in a white coat talking with a patient across a desk"
            d="M4 137 C200 130 460 135 560 150 C800 170 980 225 1097 277 L1097 660 C820 610 400 590 4 613 Z"
            fill="url(#heroTone)"/>
      <path d="M0 613 C400 585 820 598 1097 655 L1097 717 C820 650 420 612 0 628 Z" fill="var(--blue)"/>

      <path d="M110 1103 L778 1103 C740 1125 730 1157 690 1157 L122 1157 Q110 1157 110 1145 Z" fill="var(--green)"/>
      <line x1="760" y1="1103" x2="945" y2="1103" stroke="var(--green)" stroke-width="2"/>

      <path d="M445 1376 L520 1312 Q535 1300 560 1300 L1097 1300 L1097 1420 L180 1420 L225 1376 Z" fill="var(--blue)"/>
      <path d="M0 1376 L225 1376 L180 1420 L0 1420 Z" fill="var(--green)"/>
      <line x1="228" y1="1376" x2="184" y2="1420" stroke="#fff" stroke-width="2"/>
    </svg>

    <a class="site-url">www.velmoracare.example</a>

    <div class="brand">
      <div class="brand-square"></div>
      <div class="brand-name">VELMORA<br>CARE</div>
    </div>

    <p class="hero-claim"><strong>Velmora Care</strong>Tobago’s 1st<br>Private Dialysis<br>Clinic</p>

    <h1 class="headline">
      <span class="kicker">IN-CENTER</span>
      <span class="title">HEMODIALYSIS <span>Clinic</span></span>
    </h1>

    <div class="body-copy">
      <p>We offer In-center hemodialysis for renal patients who prefer to have their<br>treatments at a dialysis center.</p>
      <p>Our dialysis center has 6 Nevaro dialysis machines, supported by<br>our state of the art water purification system. Pick up and drop off of<br>patients is an additional service we offer for all in-center hemodialysis<br>patients.</p>
    </div>

    <p class="tagline">Transforming Lives, One Dialysis Session at a Time</p>

    <div class="insurance-pill">we accept<br>all insurances</div>
    <svg class="insurance-shield" viewBox="0 0 118 136" aria-hidden="true">
      <path d="M59 3 L112 22 L112 66 C112 100 88 122 59 133 C30 122 6 100 6 66 L6 22 Z" fill="#fff" stroke="var(--navy)" stroke-width="4"/>
      <path d="M59 15 L101 30 L101 66 C101 94 82 112 59 121 C36 112 17 94 17 66 L17 30 Z" fill="var(--navy)"/>
      <path d="M38 68 L53 83 L82 52" fill="none" stroke="#fff" stroke-width="9" stroke-linecap="round" stroke-linejoin="round"/>
    </svg>

    <p class="call-prompt">Call us now for more information!</p>

    <div class="phone">
      <svg viewBox="0 0 40 40" aria-hidden="true">
        <circle cx="20" cy="20" r="19" fill="#fff"/>
        <path d="M14 10 l4 0 l2 6 l-3 2 c1.5 3 3.5 5 6 6 l2 -3 l6 2 l0 4 c0 2 -2 3 -4 3 c-9 -1 -15 -7 -16 -16 c0 -2 1 -4 3 -4 z" fill="var(--blue)"/>
      </svg>
      <span>868-555-0142</span>
    </div>
  </div>
</div>
</body>
</html>
```